Tressel Linkworks Line Card

Hello - We're looking to develop a two sided brochure for our company product lines and capabilities. We're a distributor, value-added reseller, we build cable assemblies and panel assemblies. Looking for a flyer to help tell our story. Our primary market is selling to customers in the off-highway equipment markets. Construction, AG and Specialty Vehicles.

```html
<!DOCTYPE html>
<html lang="en">
<head>
<meta charset="utf-8">
<title>Tressel Linkworks Line Card</title>
<link href="https://fonts.googleapis.com/css2?family=Montserrat:wght@400;500;600;700;800&display=swap" rel="stylesheet">
<style>
  :root{
    --red:#e31e24;
    --black:#151515;
    --ink:#2a2a2a;
    --paper:#f3f3f3;
    --white:#ffffff;
    --stage:#e4e4e4;
  }
  *{box-sizing:border-box;margin:0;padding:0}
  html,body{width:894px;height:1200px;overflow:hidden;background:var(--stage)}
  body{font-family:'Montserrat',sans-serif;color:var(--ink);position:relative}

  .page{position:absolute;top:312px;width:894px;height:1200px;background:var(--paper);overflow:hidden;transform:scale(.48);transform-origin:0 0;box-shadow:0 10px 30px rgba(0,0,0,.25)}
  .page.front{left:12px}
  .page.back{left:453px}
  .page > *{position:absolute}

  .header-art{left:0;top:0}
  .brand{left:42px;top:68px;display:flex;align-items:center;gap:12px}
  .brand-mark{width:26px;height:26px;background:var(--red)}
  .brand-name{font-weight:800;font-size:34px;color:var(--black);letter-spacing:-.5px}
  .headline{left:62px;top:198px;color:var(--white);font-weight:600;font-size:29px;line-height:31px}
  .address-tab{left:475px;top:270px;width:410px;color:var(--white);font-size:15px;font-weight:500;display:flex;align-items:center;justify-content:center;gap:8px}

  .welcome-panel{left:42px;top:366px;width:810px;height:323px;background:var(--red);border-radius:10px}
  .welcome-label{left:130px;top:330px;width:634px;height:64px;background:var(--white);border:3px solid var(--red);border-radius:8px;text-align:center;padding-top:6px}
  .welcome-label .small{font-size:18px;font-weight:600;color:var(--black);line-height:22px}
  .welcome-label .big{font-size:23px;font-weight:700;color:var(--red);line-height:28px}
  .tagline{left:42px;top:412px;width:810px;text-align:center;color:var(--white);font-weight:700;font-size:15px;line-height:20px}
  .tagline span{border-bottom:2px solid var(--black);padding-bottom:2px}
  .intro{left:90px;top:462px;width:714px;text-align:center;color:var(--white);font-size:13px;line-height:17px}
  .tiles{left:62px;top:560px;width:770px;display:flex;justify-content:space-between}
  .tile{width:140px;height:128px;border:3px solid var(--white);border-radius:8px}
  .t1{background:linear-gradient(150deg,#c42a2a,#3a3a3a 70%)}
  .t2{background:linear-gradient(160deg,#4a4a46,#1e1e1e)}
  .t3{background:linear-gradient(160deg,#8a8f96,#2c2f33)}
  .t4{background:linear-gradient(160deg,#3b4a3f,#c23a3a 60%,#222)}
  .t5{background:linear-gradient(160deg,#c8c8c4,#5a5d60)}

  .card{top:712px;width:380px;height:304px;background:var(--white);border:2px solid var(--red);border-radius:8px;padding:12px 20px;overflow:hidden}
  .card.who{left:62px}
  .card.what{left:452px}
  .card h2{color:var(--red);font-size:23px;font-weight:600;padding-bottom:5px;border-bottom:2px solid var(--red);margin-bottom:9px}
  .card p{font-size:13px;line-height:16.5px;color:var(--ink)}
  .card .note{position:absolute;left:0;right:0;bottom:0;background:var(--red);color:#fde0e0;font-size:12px;line-height:15px;padding:7px 20px}

  .line-card{left:45px;top:333px;width:806px;display:flex;flex-direction:column;gap:5px}
  .line-row{display:grid;grid-template-columns:157px 245px 222px 1fr;height:62px;background:var(--white);border:2px solid var(--red);border-radius:6px;overflow:hidden}
  .line-row > div{display:flex;flex-direction:column;justify-content:center;padding:0 12px;font-size:13px;line-height:19px;color:var(--ink);border-left:1.5px solid var(--red)}
  .line-row > .maker{border-left:none;flex-direction:row;align-items:center;justify-content:flex-start;gap:7px;font-weight:700;font-size:14px;color:var(--black)}
  .maker i{width:10px;height:10px;background:var(--red);flex:none}
  .span3{grid-column:2 / 5}
  .span2{grid-column:3 / 5}

  .testimonial{left:45px;top:908px;width:806px;height:108px;border:2px solid var(--red);text-align:center;padding-top:26px}
  .testimonial .quote{position:absolute;top:-30px;font-size:60px;font-weight:800;color:var(--red);line-height:60px;background:var(--paper);padding:0 6px}
  .testimonial .q-open{left:16px}
  .testimonial .q-close{right:16px}
  .testimonial p{font-size:14px;line-height:17px;color:var(--ink);width:640px;margin:0 auto}
  .testimonial .who-said{font-size:18px;color:var(--red);margin-top:6px}

  .footer{left:0;top:1069px;width:894px;height:131px;background:var(--red)}
  .contact-tab{left:30px;top:1051px;width:182px;height:38px;background:var(--black);border-radius:8px 8px 0 0;color:var(--white);font-weight:600;font-size:17px;letter-spacing:1px;display:flex;align-items:center;justify-content:center}
  .contact-col{top:1108px;color:var(--white);font-size:15px;font-weight:500;line-height:19px}
  .contact-row{display:flex;align-items:center;gap:8px;margin-bottom:12px}
  .contact-row svg{flex:none}
  .divider{top:1100px;width:2px;height:56px;background:var(--black)}
</style>
</head>
<body>

<!-- FRONT -->
<div class="page front">
  <svg class="header-art" width="894" height="320" viewBox="0 0 894 320">
    <defs>
      <linearGradient id="photoToneA" x1="0" y1="0" x2="1" y2="1">
        <stop offset="0" stop-color="#8c1a1e"/><stop offset=".55" stop-color="#3a2a2a"/><stop offset="1" stop-color="#121212"/>
      </linearGradient>
    </defs>
    <path d="M0,188 L520,188 L620,0 L894,0 L894,309 L0,309 Z" fill="var(--red)"/>
    <g role="img" aria-label="Photo of an engineer in a red hard hat and work jacket beside large machine gears">
      <path d="M660,0 L894,0 L894,256 L540,256 Z" fill="url(#photoToneA)"/>
    </g>
    <path d="M500,256 L894,256 L894,309 L470,309 Z" fill="var(--black)"/>
  </svg>
  <div class="brand"><div class="brand-mark"></div><div class="brand-name">Tressel Linkworks</div></div>
  <div class="headline">Distribution, Contract<br>Manufacturing, and<br>System Integration</div>
  <div class="address-tab">
    <svg width="16" height="16" viewBox="0 0 16 16"><circle cx="8" cy="8" r="8" fill="var(--red)"/><path d="M8,3.5a3,3 0 0 1 3,3c0,2.2-3,5.5-3,5.5s-3-3.3-3-5.5a3,3 0 0 1 3-3z" fill="var(--white)"/></svg>
    2210 Foundry Lane Bramwell IL, 60099
  </div>

  <div class="welcome-panel"></div>
  <div class="welcome-label">
    <div class="small">WELCOME TO</div>
    <div class="big">TRESSEL LINKWORKS, INC.</div>
  </div>
  <div class="tagline">YOUR QUALITY DISTRIBUTOR OF ELECTRICAL &amp; ELECTRO-MECHANICAL<br><span>COMPONENTS &amp; ASSEMBLIES</span></div>
  <p class="intro">Tressel Linkworks Inc. was founded by Harold Vance in 1984. With innovation from second-generation sons, the family business has grown from distribution in the 1980’s, to delivering more complex solutions in the 1990’s. Change brought bigger ideas, and in 2008, Tressel Linkworks Inc. moved into a larger facility located in Bramwell, Illinois to accommodate the growing contract manufacturing business.</p>
  <div class="tiles">
    <div class="tile t1" role="img" aria-label="Photo of red battery disconnect switches"></div>
    <div class="tile t2" role="img" aria-label="Photo of a wired terminal block panel"></div>
    <div class="tile t3" role="img" aria-label="Photo of a sealed module with cable harness"></div>
    <div class="tile t4" role="img" aria-label="Photo of red wire bundles inside a cabinet"></div>
    <div class="tile t5" role="img" aria-label="Photo of an assembled control panel"></div>
  </div>

  <section class="card who">
    <h2>WHO WE ARE</h2>
    <p>Tressel Linkworks Inc.<br>was founded by Harold Vance in 1984. With innovation from second-generation sons, the family business has grown from distribution in the 1980’s, to delivering more complex solutions in the 1990’s. Change brought bigger ideas, and in 2008, Tressel Linkworks Inc. moved into a larger facility located in Bramwell, Illinois to accommodate the growing contract manufacturing business.</p>
    <div class="note">Tressel Linkworks Inc. is an ISO Certified 9001 distribution &amp; contract manufacturing business...</div>
  </section>
  <section class="card what">
    <h2>WHAT WE DO</h2>
    <p>Tressel Linkworks Inc.<br>is an ISO 9001 Certified distribution and contract manufacturing business delivering everything from processing wire leads, panel assemblies, custom box builds and wire harnesses to a variety of OEM customers. With a focus on electrical components, the family business differentiates itself from competitors by targeting different parts of the marketplace. Our online web store is evolving to meet market needs, paying close attention on delivering relevant products to our customer base.</p>
  </section>

  <div class="footer"></div>
  <div class="contact-tab">CONTACT US</div>
  <div class="contact-col" style="left:40px">
    <div class="contact-row">
      <svg width="16" height="16" viewBox="0 0 16 16"><circle cx="8" cy="8" r="8" fill="var(--white)"/><path d="M8,3.5a3,3 0 0 1 3,3c0,2.2-3,5.5-3,5.5s-3-3.3-3-5.5a3,3 0 0 1 3-3z" fill="var(--red)"/></svg>
      <span>2210 Foundry Lane<br>Bramwell IL, 60099</span>
    </div>
  </div>
  <div class="divider" style="left:262px"></div>
  <div class="contact-col" style="left:300px">
    <div class="contact-row">
      <svg width="16" height="16" viewBox="0 0 16 16"><circle cx="8" cy="8" r="8" fill="var(--white)"/><path d="M5,4.5l2,0.3 0.6,2-1.2,0.8a5,5 0 0 0 2.2,2.2l0.8-1.2 2,0.6 0.3,2c-3.5,0.6-7.3-3.2-6.7-6.7z" fill="var(--red)"/></svg>
      <span>555.014.2020</span>
    </div>
    <div class="contact-row">
      <svg width="16" height="16" viewBox="0 0 16 16"><circle cx="8" cy="8" r="8" fill="var(--white)"/><rect x="4" y="5" width="8" height="6" rx="1" fill="var(--red)"/></svg>
      <span>555.014.2026</span>
    </div>
  </div>
  <div class="divider" style="left:480px"></div>
  <div class="contact-col" style="left:518px">
    <div class="contact-row">
      <svg width="16" height="16" viewBox="0 0 16 16"><circle cx="8" cy="8" r="8" fill="var(--white)"/><rect x="4" y="5" width="8" height="6" fill="none" stroke="var(--red)" stroke-width="1.3"/><path d="M4,5 L8,8.5 L12,5" fill="none" stroke="var(--red)" stroke-width="1.3"/></svg>
      <span>sales@tressellinkworks.com</span>
    </div>
    <div class="contact-row">
      <svg width="16" height="16" viewBox="0 0 16 16"><circle cx="8" cy="8" r="8" fill="var(--white)"/><circle cx="8" cy="8" r="4.2" fill="none" stroke="var(--red)" stroke-width="1.2"/><ellipse cx="8" cy="8" rx="1.8" ry="4.2" fill="none" stroke="var(--red)" stroke-width="1"/><path d="M3.8,8 H12.2" stroke="var(--red)" stroke-width="1"/></svg>
      <span>www.tressellinkworks.com</span>
    </div>
  </div>
</div>

<!-- BACK -->
<div class="page back">
  <svg class="header-art" width="894" height="320" viewBox="0 0 894 320">
    <defs>
      <linearGradient id="photoToneB" x1="0" y1="0" x2="1" y2="1">
        <stop offset="0" stop-color="#8c1a1e"/><stop offset=".55" stop-color="#3a2a2a"/><stop offset="1" stop-color="#121212"/>
      </linearGradient>
    </defs>
    <path d="M0,188 L520,188 L620,0 L894,0 L894,309 L0,309 Z" fill="var(--red)"/>
    <g role="img" aria-label="Photo of an engineer in a red hard hat and work jacket beside large machine gears">
      <path d="M660,0 L894,0 L894,256 L540,256 Z" fill="url(#photoToneB)"/>
    </g>
    <path d="M500,256 L894,256 L894,309 L470,309 Z" fill="var(--black)"/>
  </svg>
  <div class="brand"><div class="brand-mark"></div><div class="brand-name">Tressel Linkworks</div></div>
  <div class="headline">Distribution, Contract<br>Manufacturing, and<br>System Integration</div>
  <div class="address-tab">
    <svg width="16" height="16" viewBox="0 0 16 16"><circle cx="8" cy="8" r="8" fill="var(--red)"/><path d="M8,3.5a3,3 0 0 1 3,3c0,2.2-3,5.5-3,5.5s-3-3.3-3-5.5a3,3 0 0 1 3-3z" fill="var(--white)"/></svg>
    2210 Foundry Lane Bramwell IL, 60099
  </div>

  <div class="line-card">
    <div class="line-row"><div class="maker"><i></i>Varnell Transport</div><div>Power Distribution Modules<br>Circuit Breakers</div><div>Fuses<br>Rocker &amp; Toggle Switches</div><div>CAN Switches<br>Battery Disconnects</div></div>
    <div class="line-row"><div class="maker"><i></i>Varnell Power</div><div>Battery Equalizers<br>Power Converters</div><div>True Sine Wave Inverters<br>Battery Separators</div><div>Incorrect Controllers<br>Battery Isolators</div></div>
    <div class="line-row"><div class="maker"><i></i>Brisco</div><div>Battery Disconnects<br>Battery Switches</div><div>Mono-Stable Relays</div><div>Bi-Stable Relays</div></div>
    <div class="line-row"><div class="maker"><i></i>Keldorf</div><div class="span3">On Vehicle &amp; Mobile Equipment Displays</div></div>
    <div class="line-row"><div class="maker"><i></i>Omrix</div><div>HMIs Displays<br>SCADA Software</div><div class="span2">HMI + PLC Hybrids</div></div>
    <div class="line-row"><div class="maker"><i></i>Lindqvist</div><div>DIN Valve Connectors<br>Industrial Ethernet</div><div>Connectors<br>Passive Distributors</div><div>Automation<br>Cables</div></div>
    <div class="line-row"><div class="maker"><i></i>Fusewell</div><div>Fuses<br>Fuse Blocks</div><div>Fuse Holders<br>Circuit Breakers</div><div>Resettable Fuses<br>Fuse Accessories</div></div>
    <div class="line-row"><div class="maker"><i></i>Tressel Linkworks</div><div>Custom Assemblies<br>Wire Harnesses</div><div>Testing<br>Product Integration</div><div>Custom Bus Bars<br>Kitting</div></div>
  </div>

  <div class="testimonial">
    <span class="quote q-open">“</span><span class="quote q-close">”</span>
    <p>Very professional service and quality products! Site is very user friendly with graphics and data sheets on all their products!</p>
    <p class="who-said">-Marissa T.</p>
  </div>

  <div class="footer"></div>
  <div class="contact-tab">CONTACT US</div>
  <div class="contact-col" style="left:40px">
    <div class="contact-row">
      <svg width="16" height="16" viewBox="0 0 16 16"><circle cx="8" cy="8" r="8" fill="var(--white)"/><path d="M8,3.5a3,3 0 0 1 3,3c0,2.2-3,5.5-3,5.5s-3-3.3-3-5.5a3,3 0 0 1 3-3z" fill="var(--red)"/></svg>
      <span>2210 Foundry Lane<br>Bramwell IL, 60099</span>
    </div>
  </div>
  <div class="divider" style="left:262px"></div>
  <div class="contact-col" style="left:300px">
    <div class="contact-row">
      <svg width="16" height="16" viewBox="0 0 16 16"><circle cx="8" cy="8" r="8" fill="var(--white)"/><path d="M5,4.5l2,0.3 0.6,2-1.2,0.8a5,5 0 0 0 2.2,2.2l0.8-1.2 2,0.6 0.3,2c-3.5,0.6-7.3-3.2-6.7-6.7z" fill="var(--red)"/></svg>
      <span>555.014.2020</span>
    </div>
    <div class="contact-row">
      <svg width="16" height="16" viewBox="0 0 16 16"><circle cx="8" cy="8" r="8" fill="var(--white)"/><rect x="4" y="5" width="8" height="6" rx="1" fill="var(--red)"/></svg>
      <span>555.014.2026</span>
    </div>
  </div>
  <div class="divider" style="left:480px"></div>
  <div class="contact-col" style="left:518px">
    <div class="contact-row">
      <svg width="16" height="16" viewBox="0 0 16 16"><circle cx="8" cy="8" r="8" fill="var(--white)"/><rect x="4" y="5" width="8" height="6" fill="none" stroke="var(--red)" stroke-width="1.3"/><path d="M4,5 L8,8.5 L12,5" fill="none" stroke="var(--red)" stroke-width="1.3"/></svg>
      <span>sales@tressellinkworks.com</span>
    </div>
    <div class="contact-row">
      <svg width="16" height="16" viewBox="0 0 16 16"><circle cx="8" cy="8" r="8" fill="var(--white)"/><circle cx="8" cy="8" r="4.2" fill="none" stroke="var(--red)" stroke-width="1.2"/><ellipse cx="8" cy="8" rx="1.8" ry="4.2" fill="none" stroke="var(--red)" stroke-width="1"/><path d="M3.8,8 H12.2" stroke="var(--red)" stroke-width="1"/></svg>
      <span>www.tressellinkworks.com</span>
    </div>
  </div>
</div>

</body>
</html>
```